Tide Harbor Finance Business Cards

Looking for a business card for a new mortgage broking business. Name of the business is Tide Harbor Finance. Purpose of the business is to build trust and strong relationships with clients to then assist them with your mortgage lending needs. Most relationships within the business start off as an enquiry, and then can evolve into a 10+ year relationship, servicing clients from purchasing a new home to then upgrading for their family and even then assisting their children with their first home purchase. Business card should communicate financial security and trust.

Target Market(s)

Targeting professional clients who are looking to build a relationship with a knowledgeable mortgage professional

Industry/Entity Type

Finance - Home Loans

Contact Information for Business Card

Peter Colburn, Director, mobile: 0427 903186, email:peter@tideharborfinance.com.au, website: www.tideharborfinance.com.au

Font styles to use
Sans Serif

Requirements
Must have
• On the front: Must have company logo, contact details as above. On the back: slogan, 'full of choices, free of stress', plus listing services offered: home loans, investment loans, first home buyers, refinancing, car finance

```html
<!DOCTYPE html>
<html lang="en">
<head>
<meta charset="utf-8">
<title>Tide Harbor Finance Business Cards</title>
<link rel="stylesheet" href="https://fonts.googleapis.com/css2?family=Montserrat:wght@400;500;600;700;800&display=swap">
<style>
  :root {
    --navy: #034d78;
    --navy-deep: #023f63;
    --gold: #f5a30f;
    --white: #ffffff;
    --ink: #1f2a33;
    --backdrop: #2a2a2a;
  }
  * { box-sizing: border-box; margin: 0; padding: 0; }
  html, body {
    width: 1200px; height: 800px; overflow: hidden;
    background: var(--backdrop);
    font-family: "Montserrat", sans-serif;
  }
  .stage {
    width: 1200px; height: 800px;
    display: flex; align-items: center; justify-content: center; gap: 40px;
  }
  .card {
    position: relative;
    width: 540px; height: 309px;
    border-radius: 14px;
    overflow: hidden;
  }

  /* Front */
  .card-front { background: var(--white); }
  .name-tab {
    position: absolute; left: 0; top: 92px;
    width: 14px; height: 44px;
    background: var(--navy);
    border-radius: 0 6px 6px 0;
  }
  .brand {
    position: absolute; display: flex; align-items: center; gap: 10px;
    font-weight: 700; letter-spacing: 0.02em; text-transform: uppercase;
    white-space: nowrap;
  }
  .brand-mark { width: 14px; height: 14px; border-radius: 3px; }
  .card-front .brand { right: 24px; top: 30px; color: var(--navy); font-size: 17px; }
  .card-front .brand-mark { background: var(--gold); }
  .holder { position: absolute; left: 34px; top: 90px; }
  .holder-name { color: var(--navy); font-size: 27px; font-weight: 700; line-height: 1.1; }
  .holder-role { color: var(--ink); font-size: 14px; font-weight: 500; margin-top: 4px; }
  .contacts {
    position: absolute; left: 28px; right: 20px; bottom: 24px;
    display: flex; justify-content: space-between; align-items: flex-end; gap: 16px;
  }
  .contact-list { list-style: none; display: flex; flex-direction: column; gap: 8px; }
  .contact {
    display: flex; align-items: center; gap: 7px;
    color: var(--ink); font-size: 12px; font-weight: 500;
    white-space: nowrap;
  }
  .contact-phone { font-size: 16px; }
  .icon {
    width: 18px; height: 18px; border-radius: 4px;
    background: var(--gold); display: flex; align-items: center; justify-content: center;
    flex-shrink: 0;
  }

  /* Back */
  .card-back { background: var(--navy); color: var(--white); }
  .card-back .brand {
    left: 0; right: 0; top: 58px; justify-content: center;
    color: var(--white); font-size: 24px;
  }
  .card-back .brand-mark { background: var(--gold); width: 18px; height: 18px; }
  .services-title {
    position: absolute; left: 0; right: 0; top: 118px;
    display: flex; align-items: center; justify-content: center; gap: 12px;
    font-size: 22px; font-weight: 800;
  }
  .services-title .pointer { width: 16px; height: 12px; }
  .services {
    position: absolute; left: 0; right: 0; top: 160px;
    text-align: center; font-size: 14px; font-weight: 500; line-height: 1.7;
  }
  .services .sep { color: var(--gold); margin: 0 8px; font-weight: 700; }
  .slogan-band { position: absolute; left: 0; bottom: 0; width: 540px; height: 70px; }
  .slogan {
    position: absolute; right: 0; bottom: 14px; width: 390px;
    text-align: center; color: var(--white);
    font-size: 19px; font-weight: 700; letter-spacing: 0.01em;
  }
</style>
</head>
<body>
<main class="stage">
  <section class="card card-front" aria-label="Business card front">
    <div class="brand"><span class="brand-mark"></span>Tide Harbor Finance</div>
    <span class="name-tab"></span>
    <div class="holder">
      <h1 class="holder-name">Peter Colburn</h1>
      <p class="holder-role">Director</p>
    </div>
    <div class="contacts">
      <ul class="contact-list">
        <li class="contact contact-phone">
          <span class="icon"><svg width="11" height="11" viewBox="0 0 24 24"><path fill="#fff" d="M6.6 10.8a15.1 15.1 0 0 0 6.6 6.6l2.2-2.2a1 1 0 0 1 1-.25 11.4 11.4 0 0 0 3.6.57 1 1 0 0 1 1 1V20a1 1 0 0 1-1 1A17 17 0 0 1 3 4a1 1 0 0 1 1-1h3.5a1 1 0 0 1 1 1c0 1.25.2 2.45.57 3.57a1 1 0 0 1-.25 1z"/></svg></span>
          0427 903186
        </li>
        <li class="contact">
          <span class="icon"><svg width="11" height="11" viewBox="0 0 24 24"><path fill="#fff" d="M2 11 22 3l-8 19-3-8z"/></svg></span>
          peter@tideharborfinance.com.au
        </li>
      </ul>
      <div class="contact">
        <span class="icon"><svg width="11" height="11" viewBox="0 0 24 24"><circle cx="12" cy="12" r="9" fill="none" stroke="#fff" stroke-width="2.2"/><path d="M3 12h18M12 3c3 3 3 15 0 18M12 3c-3 3-3 15 0 18" fill="none" stroke="#fff" stroke-width="1.8"/></svg></span>
        www.tideharborfinance.com.au
      </div>
    </div>
  </section>

  <section class="card card-back" aria-label="Business card back">
    <div class="brand"><span class="brand-mark"></span>Tide Harbor Finance</div>
    <h2 class="services-title">
      <svg class="pointer" viewBox="0 0 16 12"><path d="M0 6 16 0v12z" fill="var(--gold)"/></svg>
      Services Offered
      <svg class="pointer" viewBox="0 0 16 12"><path d="M16 6 0 0v12z" fill="var(--gold)"/></svg>
    </h2>
    <p class="services">
      Home Loans<span class="sep">|</span>Investment Loans<span class="sep">|</span>First Home Buyers<br>
      Refinancing<span class="sep">|</span>Car Finance
    </p>
    <svg class="slogan-band" viewBox="0 0 540 70" preserveAspectRatio="none" aria-hidden="true">
      <path d="M0 62 H130 C146 62 146 14 166 14 H500 C516 14 516 4 532 4 H540 V70 H0 Z" fill="var(--gold)"/>
    </svg>
    <p class="slogan">Full of Choices, Free of Stress</p>
  </section>
</main>
</body>
</html>
```